Harbor Current LLC

I need a business card containing the following:

HarborCurrentLLC
Certified Master Electrician
Licensed and insured
"powered by excellence"

Dale Horvath. Brian Okafor
555-014-2281 555-019-6640

HarborCurrentLLC.example

red white and blue color scheme

Industry/Entity Type

Electric Company

Contact Information for Business Card

Red white and blue coloring

Colors
ec1f27
0456a4
ffffff

Requirements
Must have
• Harbor Current
• Certified master Electrician
• Liscensed and insured
• "Powered by excellence"
• Dale Horvath. 5550142281
• Brian Okafor. 5550196640

```html
<!DOCTYPE html>
<html lang="en">
<head>
<meta charset="UTF-8">
<title>Harbor Current LLC – Business Card</title>
<link href="https://fonts.googleapis.com/css2?family=Open+Sans:wght@400;700&display=swap" rel="stylesheet">
<style>
  :root {
    --brand-red: #f23d55;
    --brand-blue: #13a8f0;
    --ink: #1d1d1f;
    --card-white: #ffffff;
    --backdrop: #e6e4e1;
  }
  * { box-sizing: border-box; margin: 0; padding: 0; }
  html, body {
    width: 1200px;
    height: 900px;
    overflow: hidden;
    background: var(--backdrop);
    font-family: "Open Sans", Arial, sans-serif;
  }
  .business-card {
    position: absolute;
    left: 75px;
    top: 150px;
    width: 1050px;
    height: 600px;
    background: var(--card-white);
    box-shadow: 0 14px 40px rgba(0,0,0,0.18);
    overflow: hidden;
  }
  .card-bands {
    position: absolute;
    inset: 0;
    width: 100%;
    height: 100%;
  }
  .company-name {
    position: absolute;
    left: 62px;
    top: 70px;
    font-size: 52px;
    font-weight: 700;
    color: var(--ink);
    letter-spacing: -0.5px;
  }
  .tagline {
    position: absolute;
    left: 62px;
    top: 188px;
    font-size: 33px;
    font-weight: 700;
    color: var(--brand-red);
  }
  .contact-names {
    position: absolute;
    left: 62px;
    top: 240px;
    font-size: 30px;
    line-height: 36px;
    color: var(--brand-blue);
  }
  .contact-list {
    position: absolute;
    left: 62px;
    top: 330px;
    list-style: none;
    font-size: 27px;
    line-height: 38px;
    color: var(--ink);
  }
  .contact-list li {
    display: flex;
    align-items: center;
    gap: 14px;
  }
  .contact-icon { width: 24px; height: 24px; flex: none; }
  .credentials {
    position: absolute;
    left: 600px;
    top: 400px;
    font-size: 29px;
    line-height: 38px;
    color: var(--ink);
  }
</style>
</head>
<body>
  <main class="business-card">
    <svg class="card-bands" viewBox="0 0 1050 600" aria-hidden="true">
      <path d="M430 0 L520 72 L960 72 Q1000 72 1050 20 L1050 0 Z" fill="var(--brand-red)"/>
      <rect x="0" y="568" width="1050" height="32" fill="var(--brand-red)"/>
      <path d="M170 600 L230 548 Q240 540 255 540 L690 540 Q710 540 722 556 L760 600 Z" fill="var(--brand-blue)"/>
    </svg>

    <h1 class="company-name">Harbor Current LLC</h1>
    <p class="tagline">“Powered by excellence”</p>

    <p class="contact-names">Dale Horvath<br>Brian Okafor</p>

    <ul class="contact-list">
      <li>
        <svg class="contact-icon" viewBox="0 0 24 24"><circle cx="12" cy="12" r="12" fill="var(--brand-blue)"/><path d="M8 6 l2.5 0 l1 3 l-1.5 1.2 q1 2.3 3.3 3.3 l1.2-1.5 l3 1 l0 2.5 q-7 1 -9.5-9.5z" fill="#fff"/></svg>
        555-014-2281
      </li>
      <li>
        <svg class="contact-icon" viewBox="0 0 24 24"><circle cx="12" cy="12" r="12" fill="var(--brand-blue)"/><rect x="8.5" y="5.5" width="7" height="13" rx="1.5" fill="none" stroke="#fff" stroke-width="1.8"/><circle cx="12" cy="16" r="1" fill="#fff"/></svg>
        555-019-6640
      </li>
      <li>
        <svg class="contact-icon" viewBox="0 0 24 24"><circle cx="12" cy="12" r="10.5" fill="none" stroke="var(--brand-blue)" stroke-width="2"/><ellipse cx="12" cy="12" rx="4.5" ry="10.5" fill="none" stroke="var(--brand-blue)" stroke-width="1.6"/><path d="M1.5 12 H22.5 M3.5 6.5 H20.5 M3.5 17.5 H20.5" stroke="var(--brand-blue)" stroke-width="1.6"/></svg>
        www.harborcurrentLLC.example
      </li>
    </ul>

    <p class="credentials">HarborCurrent<br>Certified Master Electrician<br>Licensed and insured</p>
  </main>
</body>
</html>
```